Guaranteed Job - Sleek Sexy Business Card UV Spot

Im looking for a sleek and sexy business card, that resembles elite or VIP status status.
our business is corinvale.example
you can view our products on there, but our main audience for handing out our cards will be for people in the hospitality industry, so it will need to impress high management and CEO of hotels and restaurants, bars, clubs etc...
the card features will have UV spot on both sides, 400gsm stock. standard size.
Artwork should be 86 x 54mm + 2mm bleed = 90 x 58mm
it should have a nice "unique" uv spot pattern that highlights the card, not a repeated pattern, theres no originality there, and it will be disregarded.
The written material will be:
Corin Vale Hospitality College (logo)
Tobin Marsh
Director
Phone: 1300 615 737
Mobile: 0455 817 296
Email: info@corinvale.example
website: www.corinvale.example
I'm looking for originality here, i don't want just a simple stock card, want something that has a wow factor for people.
You will find the logo attached. you may invert the white to black words to suit the background as you please.
thank you and good luck
As a side note, ive received a lot of proposals, im too busy to give feedback to each and every one, so if i havent provided feedback for your design within 24 hours, then consider it not acceptable, and you could resubmit another design.
So far i have not seen any design that stood out for me, they all seem pretty generic. there nothing thats unique, i would figure for the amount that im offering, that people would put some more effort and creativity into the design.
so far over 200 designs submitted, and nothing i have seen looks very original, everything looks like a different variation of the same stuff, i said it very clearly i wanted something unique, the only thing that has come close to it so far is this one
Reason: Ive received alot of design concepts and i have reviewed everyone, but i havent had time to give feedback to every single one, only the ones that have interested me, if i havent responded, its because i havent found it good enough.
so far only a few design have been on par with what ive been looking for, an attractive eye popping design.
heres a few of them,
http://files.pixelbazaar.example/design_img/51736/62418/62418_2840915_51736_image.jpg
http://files.pixelbazaar.example/design_img/51736/68254/68254_2841377_51736_image.jpg
theyre, both unique and original, and eye catching, the only thing theyre missing is the sexyness.
if you still think you have some creativity left in your minds, then throw it on here.
Reason: Sorry guys for the delay, I was in a serious accident and out of commission for the past few months, I'm just slowly recovering now, please bare with me as i try to attend to this project, it may take me awhile as I have other projects that are on standby, I'm not 100% at the moment, so im extending the deadline for 2 weeks right now. Thanks for your patience.
Hospitality

```html
<!DOCTYPE html>
<html lang="en">
<head>
<meta charset="utf-8">
<title>Corin Vale Hospitality College – Business Card</title>
<link rel="stylesheet" href="https://fonts.googleapis.com/css2?family=Roboto:wght@400;700&display=swap">
<style>
  :root {
    --page: #e9e9eb;
    --card: #070708;
    --band: #0b0b0c;
    --pattern-dark: #1d1e21;
    --pattern-mid: #2c2e33;
    --pattern-blue: #2f6f95;
    --accent: #4aa8dc;
    --ink: #ffffff;
    --ink-soft: #c9cdd2;
  }
  * { box-sizing: border-box; margin: 0; padding: 0; }
  html, body {
    width: 1200px; height: 900px; overflow: hidden;
    background: var(--page);
    font-family: "Roboto", Arial, sans-serif;
  }
  .sheet {
    position: relative; width: 1200px; height: 900px;
    display: flex; flex-direction: column; align-items: center; justify-content: center; gap: 40px;
  }
  .card {
    position: relative; width: 640px; height: 400px;
    background: var(--card); overflow: hidden;
    box-shadow: 0 6px 18px rgba(0,0,0,.18);
  }
  .card-pattern {
    position: absolute; inset: 0;
    background:
      linear-gradient(135deg, var(--pattern-mid) 0%, var(--pattern-dark) 35%, var(--pattern-blue) 55%, var(--pattern-dark) 75%, var(--pattern-mid) 100%);
    opacity: .9;
  }
  /* Back side */
  .back-band {
    position: absolute; left: -60px; top: 150px; width: 780px; height: 120px;
    background: var(--band); transform: rotate(-14deg);
    box-shadow: 0 0 30px rgba(0,0,0,.6);
  }
  .back-brand {
    position: absolute; left: 175px; top: 160px;
    transform: rotate(-14deg); transform-origin: left top;
    display: flex; align-items: center; gap: 14px;
  }
  .brand-mark { width: 30px; height: 30px; background: var(--accent); flex: none; }
  .brand-name {
    color: var(--ink); font-weight: 700; font-size: 34px; letter-spacing: 1px; line-height: 1;
    text-transform: uppercase;
  }
  .brand-sub {
    color: var(--ink); font-weight: 700; font-size: 11px; letter-spacing: 2px;
    text-transform: uppercase; margin-top: 5px;
  }
  .brand-url { color: var(--ink); font-weight: 700; font-size: 15px; margin-top: 6px; }
  /* Front side */
  .front-pattern {
    position: absolute; inset: 0;
    clip-path: polygon(0 30%, 12% 30%, 12% 44%, 24% 44%, 24% 56%, 36% 56%, 36% 68%, 48% 68%, 48% 78%, 62% 78%, 62% 88%, 78% 88%, 78% 100%, 0 100%);
  }
  .front-brand {
    position: absolute; left: 330px; top: 44px;
    display: flex; align-items: center; gap: 12px;
  }
  .front-brand .brand-name { font-size: 26px; }
  .front-brand .brand-sub { font-size: 9px; }
  .person { position: absolute; left: 370px; top: 118px; }
  .person-name { color: var(--accent); font-weight: 700; font-size: 26px; }
  .person-role { color: var(--ink); font-size: 14px; margin-top: 2px; margin-left: 60px; }
  .contacts {
    position: absolute; right: 40px; top: 190px;
    color: var(--ink); font-weight: 700; font-size: 15px; line-height: 1.45; text-align: left;
  }
  .contacts .label { color: var(--accent); margin-right: 4px; }
  .contacts .indent { padding-left: 70px; }
</style>
</head>
<body>
<main class="sheet">
  <section class="card card-back" aria-label="Business card, back">
    <div class="card-pattern" role="img" aria-label="Spot-UV pattern of repeated brand name in grey and blue"></div>
    <div class="back-band"></div>
    <div class="back-brand">
      <span class="brand-mark"></span>
      <div>
        <div class="brand-name">Corin Vale</div>
        <div class="brand-sub">Hospitality College</div>
        <div class="brand-url">www.corinvale.example</div>
      </div>
    </div>
  </section>

  <section class="card card-front" aria-label="Business card, front">
    <div class="card-pattern front-pattern" role="img" aria-label="Stepped spot-UV pattern of repeated brand name in grey and blue"></div>
    <div class="front-brand">
      <span class="brand-mark"></span>
      <div>
        <div class="brand-name">Corin Vale</div>
        <div class="brand-sub">Hospitality College</div>
      </div>
    </div>
    <div class="person">
      <div class="person-name">Tobin Marsh</div>
      <div class="person-role">Director</div>
    </div>
    <div class="contacts">
      <div class="indent"><span class="label">p:</span>1300 615 737</div>
      <div class="indent"><span class="label">m:</span>0455 817 296</div>
      <div><span class="label">e:</span>info@corinvale.example</div>
      <div><span class="label">w:</span>www.corinvale.example</div>
    </div>
  </section>
</main>
</body>
</html>
```